Business Cards for an 'affordable luxury' inner city home builder in Calgary.

We need a business card design that emulates the progressive, innovative, culture of our company and the modern style of our homes. Use our website www.velmarcrest-ab.com as a reference for the product we build.

Our company builds homes in the inner city space of Calgary, Alberta. We build affordable luxury.

Target Market(s)

Young professional Families

Contact Information for Business Card

Try to maintain consistency with the logo font and the card font.

Requirements
Must have
• The details must include: Name, education, title, phone number, website and email (Address is not as important)
• The design must be uniques (like our logo), elegant, sophisticated and modern.

```html
<!DOCTYPE html>
<html lang="en">
<head>
<meta charset="utf-8">
<title>Velmarcrest Homes Ltd – Business Card</title>
<link rel="stylesheet" href="https://fonts.googleapis.com/css2?family=Open+Sans:wght@400;700&family=PT+Sans+Narrow:wght@400&display=swap">
<style>
  :root {
    --backdrop: #9a9a9a;
    --paper: #ffffff;
    --ink: #222222;
    --ink-soft: #555555;
    --band-dark: #1e1e1e;
    --band-mid: #8a8a8a;
    --band-light: #c4c4c4;
    --divider: #9c9c9c;
    --reverse-bg: #232323;
    --reverse-ink: #ffffff;
  }
  * { margin: 0; padding: 0; box-sizing: border-box; }
  html, body {
    width: 1133px; height: 1200px; overflow: hidden;
    background: var(--backdrop);
  }
  .canvas { position: relative; width: 1133px; height: 1200px; }

  .card { position: absolute; left: 218px; width: 697px; height: 398px; }

  /* Front */
  .card-front { top: 153px; background: var(--paper); }
  .brand {
    position: absolute; left: 78px; top: 168px;
    display: flex; align-items: center; gap: 16px;
  }
  .brand-square { width: 34px; height: 34px; background: var(--ink); }
  .brand-name {
    font-family: "Open Sans", sans-serif; font-weight: 400;
    font-size: 18px; line-height: 21px; letter-spacing: 0.5px;
    color: var(--ink); text-transform: uppercase;
  }
  .divider {
    position: absolute; left: 357px; top: 76px;
    width: 2px; height: 250px; background: var(--divider);
  }
  .details { position: absolute; left: 382px; top: 80px; color: var(--ink); }
  .person-name {
    font-family: "Open Sans", sans-serif; font-weight: 700;
    font-size: 24px; line-height: 30px; margin-bottom: 4px;
  }
  .credentials {
    list-style: none;
    font-family: "PT Sans Narrow", sans-serif; font-size: 18px; line-height: 22px;
    color: var(--ink);
  }
  .address {
    font-family: "Open Sans", sans-serif; font-size: 16px;
    color: var(--ink-soft); margin-top: 16px; margin-bottom: 8px;
  }
  .contact-list { list-style: none; }
  .contact-item {
    display: flex; align-items: center; gap: 8px;
    font-family: "Open Sans", sans-serif; font-size: 16px; line-height: 23px;
    color: var(--ink-soft);
  }
  .contact-icon { width: 16px; height: 16px; flex: none; }
  .band-row {
    position: absolute; left: 0; bottom: 0; width: 100%; height: 14px;
    display: flex; gap: 2px;
  }
  .band { flex: 1; }
  .band-dark { background: var(--band-dark); }
  .band-mid { background: var(--band-mid); }
  .band-light { background: var(--band-light); }

  /* Back */
  .card-back { top: 647px; background: var(--reverse-bg); }
  .reverse-brand {
    position: absolute; left: 0; right: 0; top: 150px;
    display: flex; justify-content: center; align-items: center; gap: 18px;
  }
  .reverse-square { width: 40px; height: 40px; background: var(--reverse-ink); }
  .reverse-name {
    font-family: "Open Sans", sans-serif; font-weight: 400;
    font-size: 34px; letter-spacing: 4px; color: var(--reverse-ink);
    text-transform: uppercase;
  }
  .reverse-web {
    position: absolute; left: 0; right: 0; top: 350px; text-align: center;
    font-family: "Open Sans", sans-serif; font-size: 18px;
    letter-spacing: 7px; color: var(--reverse-ink);
  }
</style>
</head>
<body>
<main class="canvas">
  <section class="card card-front">
    <div class="brand">
      <span class="brand-square"></span>
      <span class="brand-name">Velmarcrest<br>Homes Ltd</span>
    </div>
    <div class="divider"></div>
    <div class="details">
      <h1 class="person-name">Delsyn</h1>
      <ul class="credentials">
        <li>Co-Founder</li>
        <li>Business Development / Strategy</li>
        <li>Professional Engineer (P.ENG)</li>
        <li>Masters of Business Administration (MBA)</li>
      </ul>
      <p class="address">482 17 Ave NE, Calgary, AB</p>
      <ul class="contact-list">
        <li class="contact-item">
          <svg class="contact-icon" viewBox="0 0 16 16" aria-hidden="true"><path fill="#222" d="M2 5c0-2 2-3 6-3s6 1 6 3v1h-3V5H5v1H2zM4 7h8l2 7H2zM8 9a2 2 0 100 4 2 2 0 000-4z"/></svg>
          <span>403-555-0148</span>
        </li>
        <li class="contact-item">
          <svg class="contact-icon" viewBox="0 0 16 16" aria-hidden="true"><path fill="#222" d="M1 4h14v9H1zM1 4l7 5 7-5v1.3L8 10.3 1 5.3z"/><path fill="#fff" d="M1.6 4.6h12.8L8 9.2z"/></svg>
          <span>projects@velmarcrest-ab.com</span>
        </li>
        <li class="contact-item">
          <svg class="contact-icon" viewBox="0 0 16 16" aria-hidden="true"><circle cx="8" cy="8" r="7" fill="#222"/><path fill="#fff" d="M5 4c2 0 3 1 2 3s-3 1-3 3-1 1-1 0 0-4 2-6zM10 9c1 0 2 1 1 3s-2 0-1-3z"/></svg>
          <span>www.velmarcrest-ab.com</span>
        </li>
      </ul>
    </div>
    <div class="band-row">
      <span class="band band-dark"></span>
      <span class="band band-mid"></span>
      <span class="band band-light"></span>
    </div>
  </section>

  <section class="card card-back">
    <div class="reverse-brand">
      <span class="reverse-square"></span>
      <span class="reverse-name">Velmarcrest</span>
    </div>
    <p class="reverse-web">www.velmarcrest-ab.com</p>
  </section>
</main>
</body>
</html>
```